Business Card

I would like a business card with a picture of my husband and I that is unique and professional.

Industry/Entity Type

Business

Font styles to use
Serif

```html
<!DOCTYPE html>
<html lang="en">
<head>
<meta charset="utf-8">
<title>Dana Whitfield – Business Card</title>
<link rel="stylesheet" href="https://fonts.googleapis.com/css2?family=Michroma&family=Roboto+Condensed:wght@400&family=Roboto:wght@400&family=Oswald:wght@500&display=swap">
<style>
  :root {
    --stage-top: #8a8a8a;
    --stage-bottom: #3a3a3a;
    --card-yellow: #f4f29b;
    --card-black: #1f1f1f;
    --accent-gold: #f0c266;
    --ink: #1b1b1b;
    --paper: #ffffff;
    --contact: #f2f2f2;
    --photo-light: #8c8c8c;
    --photo-dark: #3d3d3d;
  }
  * { box-sizing: border-box; margin: 0; padding: 0; }
  html, body { width: 1200px; height: 1000px; overflow: hidden; }
  body {
    background: linear-gradient(160deg, var(--stage-top), var(--stage-bottom));
    position: relative;
  }
  .card {
    position: absolute;
    top: 68px;
    width: 544px;
    height: 318px;
    overflow: hidden;
    box-shadow: 0 2px 6px rgba(0,0,0,.35);
  }
  .card--front { left: 44px; background: var(--card-yellow); }
  .card--back { left: 618px; background: var(--paper); }

  .front__band { position: absolute; inset: 0; width: 100%; height: 100%; }
  .front__name {
    position: absolute; left: 59px; top: 35px;
    font: 400 23px/1 "Michroma", sans-serif;
    color: var(--ink); letter-spacing: .5px;
  }
  .front__title {
    position: absolute; left: 59px; top: 63px;
    font: 400 14px/1 "Roboto Condensed", sans-serif;
    color: var(--ink);
  }
  .front__contact {
    position: absolute; left: 60px; top: 224px;
    list-style: none;
    font: 400 15px/1 "Roboto", sans-serif;
    color: var(--contact);
  }
  .front__contact li { display: flex; align-items: center; gap: 8px; margin-bottom: 11px; }
  .front__contact svg { width: 11px; height: 11px; fill: var(--contact); }
  .front__photo {
    position: absolute; left: 362px; top: 48px; width: 182px; height: 270px;
    background: linear-gradient(180deg, var(--photo-light), var(--photo-dark));
    border-radius: 70px 60px 0 0;
  }

  .back__mark {
    position: absolute; left: 50%; top: 62px; transform: translateX(-50%);
    display: flex; flex-direction: column; align-items: center; gap: 16px;
  }
  .back__dot {
    width: 104px; height: 104px; border-radius: 50%;
    background: var(--card-black);
  }
  .back__wordmark {
    font: 500 22px/1 "Oswald", sans-serif;
    color: var(--ink);
    letter-spacing: .8px;
  }
  .back__company {
    position: absolute; left: 50%; top: 258px; transform: translateX(-50%);
    white-space: nowrap; text-align: center;
    font: 500 13px/1 "Oswald", sans-serif;
    color: var(--ink); letter-spacing: .8px; text-transform: uppercase;
  }
  .back__rule {
    display: block; margin: 5px auto 0; width: 256px; height: 6px;
  }
</style>
</head>
<body>
  <section class="card card--front">
    <svg class="front__band" viewBox="0 0 544 318" preserveAspectRatio="none" aria-hidden="true">
      <path d="M0 178 Q260 150 544 160 L544 318 L0 318 Z" fill="var(--accent-gold)"/>
      <path d="M0 186 Q260 158 544 168 L544 318 L0 318 Z" fill="var(--card-black)"/>
    </svg>
    <h1 class="front__name">Dana Whitfield</h1>
    <p class="front__title">Professional Mentorship Strategist</p>
    <ul class="front__contact">
      <li>
        <svg viewBox="0 0 24 24"><path d="M6.6 10.8a15.1 15.1 0 0 0 6.6 6.6l2.2-2.2a1 1 0 0 1 1-.25 11.4 11.4 0 0 0 3.6.57 1 1 0 0 1 1 1V20a1 1 0 0 1-1 1A17 17 0 0 1 3 4a1 1 0 0 1 1-1h3.5a1 1 0 0 1 1 1c0 1.25.2 2.45.57 3.57a1 1 0 0 1-.25 1z"/></svg>
        555-214-8830
      </li>
      <li>
        <svg viewBox="0 0 24 24"><path d="M2 6h20v12H2z M2 6l10 7 10-7" stroke="var(--card-black)" stroke-width="1.5"/></svg>
        DanaWhitfield@example.com
      </li>
    </ul>
    <div class="front__photo" role="img" aria-label="Portrait photo of the couple in grey suits, smiling"></div>
  </section>

  <section class="card card--back">
    <div class="back__mark">
      <span class="back__dot" aria-hidden="true"></span>
      <span class="back__wordmark">Whitfield</span>
    </div>
    <p class="back__company">
      Whitfield Leadership Development
      <svg class="back__rule" viewBox="0 0 256 6" aria-hidden="true">
        <line x1="0" y1="3" x2="256" y2="3" stroke="var(--ink)" stroke-width="1"/>
      </svg>
    </p>
  </section>
</body>
</html>
```